Modern Billboard Ad for Criminal Defense Firm

10.5 x 36 We're looking for something to set us apart from the local competition. Looking for sleek and modern. We're a mid-sized firm in a small market city. We want to give the artist room to be creative on this one.
Thanks

Target Market(s)

Adult clients who have been charged with a crime/DWI

Industry/Entity Type

legal

Font styles to use
Serif
Sans Serif

Requirements
Must have
• Needs to have the firm name in large lettering. Law Offices of Marcus T Whitfield. “PLLC” does not have to be included. Phone number of (555) 384-1927 should be included but not the main focus.
Nice to have
• A call to action or something similar. “Don’t go it alone, call today.”, “ Arrested?”

```html
<!DOCTYPE html>
<html lang="en">
<head>
<meta charset="utf-8">
<title>Law Offices of Marcus T Whitfield – Billboard</title>
<link href="https://fonts.googleapis.com/css2?family=EB+Garamond:ital,wght@0,500;0,700;1,400&display=swap" rel="stylesheet">
<style>
  :root {
    --forest: #0a4528;
    --gold: #d4ae36;
    --white: #ffffff;
    --badge-dark: #262626;
    --badge-blue: #2aa8df;
    --photo-a: #5a4a3c;
    --photo-b: #3d2a32;
    --photo-c: #7d8078;
  }
  html, body {
    margin: 0;
    padding: 0;
    overflow: hidden;
    background: #ffffff;
  }
  .billboard {
    position: relative;
    width: 1200px;
    height: 350px;
    overflow: hidden;
    background: var(--forest);
    font-family: "EB Garamond", Georgia, serif;
  }
  .gold-panel {
    position: absolute;
    left: 880px;
    top: 0;
    width: 320px;
    height: 350px;
    background: var(--gold);
  }
  .accent-curve {
    position: absolute;
    left: 0;
    top: 270px;
  }
  .award-card {
    position: absolute;
    left: 39px;
    top: 83px;
    width: 136px;
    height: 300px;
    background: var(--white);
    border-radius: 19px;
  }
  .award-badge {
    position: absolute;
    left: 11px;
    top: 21px;
    width: 108px;
    height: 158px;
    background: var(--badge-dark);
    border: 3px solid var(--badge-blue);
  }
  .firm-name {
    position: absolute;
    right: 518px;
    top: 30px;
    margin: 0;
    color: var(--gold);
    font-weight: 700;
    font-size: 54px;
    line-height: 62px;
    text-align: right;
    white-space: nowrap;
    letter-spacing: -0.5px;
  }
  .phone-band {
    position: absolute;
    left: 386px;
    top: 172px;
  }
  .phone {
    position: absolute;
    right: 521px;
    top: 180px;
    margin: 0;
    color: var(--white);
    font-weight: 500;
    font-size: 38px;
    line-height: 46px;
    white-space: nowrap;
  }
  .cta {
    position: absolute;
    right: 521px;
    top: 236px;
    margin: 0;
    color: var(--white);
    font-style: italic;
    font-weight: 400;
    font-size: 34px;
    line-height: 42px;
    text-align: right;
    white-space: nowrap;
  }
  .attorney-photo {
    position: absolute;
    left: 701px;
    top: 19px;
    width: 304px;
    height: 303px;
    border-radius: 28px;
    background: linear-gradient(135deg, var(--photo-a) 0%, var(--photo-b) 45%, var(--photo-c) 100%);
  }
</style>
</head>
<body>
  <div class="billboard">
    <div class="gold-panel"></div>

    <svg class="accent-curve" width="60" height="20" viewBox="0 0 60 20" aria-hidden="true">
      <path d="M0 15 Q20 7 40 10" fill="none" stroke="var(--gold)" stroke-width="1"/>
    </svg>

    <div class="award-card">
      <div class="award-badge" role="img" aria-label="Community choice award badge"></div>
    </div>

    <h1 class="firm-name">Law Offices<br>of Marcus T Whitfield</h1>

    <svg class="phone-band" width="316" height="61" viewBox="0 0 316 61" aria-hidden="true">
      <path d="M0 61 L20 14 Q26 0 42 0 L316 0 L316 61 Z" fill="var(--gold)"/>
    </svg>
    <p class="phone">(555) 384-1927</p>

    <p class="cta">Don’t go it alone, call today!<br>Arrested?</p>

    <div class="attorney-photo" role="img" aria-label="Portrait photo of the attorney in a grey suit in front of foliage"></div>
  </div>
</body>
</html>
```